Geschäftspapiere für Unternehmen aus Not- und Sicherheitsbeleuchtungsbranche
Zielgruppe
Wir sind ein Unternehmen der Not- und Sicherheitsbeleuchtungsbranche und arbeiten vornehmlich mit dem deutschen Elektrogroßhandel zusammen.
Aufgabenstellung
WIr möchten nicht nur Schreibblöcke drucken, wir benötigen die Vorlage auch als Word-Datei für Geschäftsbriefe.
Orientierung und Farbwahl gemäß unserer Website. Im Anhang finden Sie bereits das aktuelle Briefdesign. Dieses verbraucht jedoch zu viel Platz und liegt uns nicht als Word vor. Die Daten können übernommen werden, ergänzt muss noch die UST-ID werden: DE718206359

```html
<!DOCTYPE html>
<html lang="de">
<head>
<meta charset="utf-8">
<title>Briefbogen – Torvanel</title>
<link rel="stylesheet" href="https://fonts.googleapis.com/css2?family=Questrial&display=swap">
<style>
  :root {
    --paper: #ffffff;
    --brand-magenta: #b0066a;
    --brand-slate: #5f6872;
    --watermark: #ebebed;
  }
  html, body {
    margin: 0;
    padding: 0;
    width: 887px;
    height: 1200px;
    overflow: hidden;
    background: var(--paper);
  }
  .letterhead {
    position: relative;
    width: 887px;
    height: 1200px;
    background: var(--paper);
    font-family: "Questrial", "Helvetica Neue", Arial, sans-serif;
  }
  .brand-mark {
    position: absolute;
    top: 35px;
    left: 657px;
    height: 78px;
    display: flex;
    align-items: center;
    gap: 10px;
  }
  .brand-mark__square {
    width: 78px;
    height: 78px;
    border: 5px solid var(--brand-slate);
    box-sizing: border-box;
    flex: none;
  }
  .brand-mark__name {
    font-size: 19px;
    letter-spacing: 1.5px;
    color: var(--brand-slate);
    line-height: 1;
    white-space: nowrap;
  }
  .watermark {
    position: absolute;
    top: 522px;
    left: 158px;
    height: 255px;
    display: flex;
    align-items: center;
    gap: 20px;
  }
  .watermark__square {
    width: 255px;
    height: 255px;
    border: 19px solid var(--watermark);
    box-sizing: border-box;
    flex: none;
  }
  .watermark__name {
    font-size: 58px;
    letter-spacing: 3px;
    color: var(--watermark);
    line-height: 1;
    white-space: nowrap;
  }
  .footer-bands {
    position: absolute;
    left: 0;
    bottom: 0;
    width: 887px;
    height: 43px;
    display: block;
  }
  .footer-bands__accent { fill: var(--brand-magenta); }
  .footer-bands__base { fill: var(--brand-slate); }
</style>
</head>
<body>
  <main class="letterhead">
    <header class="brand-mark">
      <span class="brand-mark__square"></span>
      <span class="brand-mark__name">TORVANEL</span>
    </header>

    <div class="watermark" aria-hidden="true">
      <span class="watermark__square"></span>
      <span class="watermark__name">TORVANEL</span>
    </div>

    <svg class="footer-bands" viewBox="0 0 887 43" preserveAspectRatio="none" aria-hidden="true">
      <polygon class="footer-bands__accent" points="0,22 317,22 302,43 0,43"/>
      <polygon class="footer-bands__base" points="347,0 887,0 887,43 315,43"/>
    </svg>
  </main>
</body>
</html>
```